Corporate Business Card

Very professional, Modern, Not to busy, include phone address email, website
(253) 555-0174, 61807 19th Street N, Kent, WA 98517, marcus@kestrelbayholding.com, brelvanindustries.com

Target Market(s)

Manufacturing

Industry/Entity Type

Aero, machining, manufacturing, Off road racing

Contact Information for Business Card

Phone, address email, website

```html
<!DOCTYPE html>
<html lang="en">
<head>
<meta charset="utf-8">
<title>Brelvan Industries – Business Card</title>
<link href="https://fonts.googleapis.com/css2?family=Montserrat:wght@500;700&display=swap" rel="stylesheet">
<style>
  :root {
    --navy: #161e52;
    --red: #d90000;
    --white: #ffffff;
    --backdrop: #e5e5e5;
  }
  * { margin: 0; padding: 0; box-sizing: border-box; }
  html, body {
    width: 1200px; height: 1000px; overflow: hidden;
    background: var(--backdrop);
    font-family: "Montserrat", Arial, sans-serif;
  }
  .canvas { position: relative; width: 1200px; height: 1000px; }

  .card {
    position: absolute; left: 344px; width: 510px; height: 291px;
    overflow: hidden;
    box-shadow: 0 8px 16px rgba(0,0,0,0.28);
  }
  .card-front {
    top: 180px; background: var(--navy);
    border-radius: 0 36px 0 36px;
  }
  .card-back {
    top: 528px; background: var(--white);
    border-radius: 36px 0 36px 0;
  }

  .front-brand {
    position: absolute; left: 0; right: 0; top: 110px;
    text-align: center; color: var(--white); font-weight: 700;
  }
  .front-brand .brand-name { display: block; font-size: 44px; letter-spacing: 2px; line-height: 1; }
  .front-brand .brand-sub { display: block; font-size: 15px; letter-spacing: 6px; margin-top: 8px; }

  .holder-name {
    position: absolute; left: 28px; top: 44px;
    font-size: 19px; font-weight: 700; color: var(--navy); line-height: 1;
  }
  .holder-title {
    position: absolute; left: 28px; top: 65px;
    font-size: 19px; font-weight: 700; color: var(--red); line-height: 1;
  }
  .contact-list {
    position: absolute; left: 28px; top: 137px; list-style: none;
    font-size: 15.5px; font-weight: 500; color: var(--navy);
  }
  .contact-list li { height: 27px; line-height: 27px; }

  .back-brand {
    position: absolute; left: 438px; top: 35px; width: 48px; height: 176px;
  }
  .back-brand .brand-vertical {
    position: absolute; left: 50%; top: 50%;
    transform: translate(-50%, -50%) rotate(-90deg);
    white-space: nowrap; font-size: 17px; font-weight: 700;
    letter-spacing: 1px; color: var(--navy);
  }

  .web-band {
    position: absolute; left: 0; right: 0; bottom: 0; height: 50px;
    background: var(--red); color: var(--white);
    font-size: 15px; font-weight: 500; line-height: 50px; padding-left: 35px;
  }

  .corner-brand {
    position: absolute; left: 977px; top: 922px;
    color: var(--navy); font-weight: 700; text-align: right; line-height: 1;
  }
  .corner-brand .brand-name { display: block; font-size: 28px; letter-spacing: 1px; }
  .corner-brand .brand-sub { display: block; font-size: 10px; letter-spacing: 4px; margin-top: 5px; }
</style>
</head>
<body>
<main class="canvas">
  <section class="card card-front" aria-label="Card front">
    <div class="front-brand">
      <span class="brand-name">BRELVAN</span>
      <span class="brand-sub">INDUSTRIES</span>
    </div>
  </section>

  <section class="card card-back" aria-label="Card back">
    <p class="holder-name">FIRSTNAME LASTNAME</p>
    <p class="holder-title">TITLE/POSITION</p>
    <ul class="contact-list">
      <li>(253) 555-0174</li>
      <li>marcus@kestrelbayholding.com</li>
      <li>61807 19th Street N, Kent, WA 98517</li>
    </ul>
    <div class="back-brand">
      <span class="brand-vertical">BRELVAN INDUSTRIES</span>
    </div>
    <div class="web-band">brelvanindustries.com</div>
  </section>

  <div class="corner-brand">
    <span class="brand-name">BRELVAN</span>
    <span class="brand-sub">INDUSTRIES</span>
  </div>
</main>
</body>
</html>
```